Varubo Highlands coffee needs bold, new coffee pack design

Having just developed a new logo (see attached file), we are now in the process of developing new coffee bag packaging designs. We are using a custom bag printer in the US, so the design will need will need to follow a specific art spec/template (which has also been uploaded). We will eventually need designs for two different coffee brands/types and two different size bags (essentially a 250g and 500g size). At this point, however, our goal is to develop a design for one size/coffee brand and from there work on variations for the others.
Updates

Project Deadline Extended
Reason: We are considering some small changes to the original design we outlined and want to allow extra time for current and new designers to make those tweaks. Thanks for your consideration of our coffee package project!

Hello, After reviewing some designs so far, and receiving additional feedback from test users in our market, we are making some changes to the template design. I have uploaded a new version of the template content, which has the following changes. 1. The two side panels are now without any text, but a visual design/pattern that you want to try there is still welcome. 2. The front and bag sections has been cleaned up a bit to have less text and more room for a visual design. 3. We would like to see stronger user of the following colors: red, yellow, black (which are Ugandan flag colors) and white. Some green as needed is allowed. 4. I have uploaded a map file showing Uganda including the Varubo region where the coffee comes from. Would like to incorporate this on the back side, ideally with a small Varubo Highlands logo pointing to the region in the bottom left in green or could even say something like "Home of Varubo Highlands Coffee.". Also the country should be titled "Uganda" to make that clear. With these changes, if you need more time on the design, let me know and we can look at extending the deadline. Thank you!

Hello, Although it is not showing just yet, we expect to have a one-week extension for this contest (so not ending on 29 September, but October 6). If you are working on a design, or re-design, please continue to do so as the contest will be extended. If you are interested in starting work, please do so. Thanks for your interest in our package design contest and I look forward to seeing your work soon. Doriel

Hello, Thank you to everyone who has submitted designs so far. We want to highlight two important items at this point: 1. Based on user feedback, we are changing the design considerations bit. The size and shape of the bags are not changing, but some of the creative content is. A new file has been uploaded entitled Coffee package content 250g size v3.pdf which details these changes. Please download and read that for updates. If you have any questions, please let me know. 2. Due to these changes, we are extending this contest for another week, so I'm hopeful you will have time to make changes and submit your new ideas! Thank you, Doriel

Target Market(s)

Varubo Highlands is a premium Ugandan coffee. We are targeting those drinkers who appreciate and seek out great coffee.

Industry/Entity Type

Printer

Font styles to use
Sans Serif

Colors
ec1f27
ffffff
9bcb3c
ffcf3e

Requirements
Must have
• The attached PDF file (coffee package content) design and content elements that need to be included. Designer has strong license to determine HOW they should be designed and shown. In terms of colors, would like to see strong use of red, black, yellow (Ugandan flag colors) and white. Green is also an option if needed.

The design file will need to follow specs that are detailed here:
http://www.pelmacrate.com/artwork_specs and be in the format shown in the uploaded file 5-8 oz Bag Template.pdf.
Nice to have
• Bag should be simple, but elegant. We did testing and found that too much information was distracting so we have pared down the design/content elements to the basics. Still, creative elements or patterns and overlays are very welcome.
Should not have
• The tone should be elegant and creative, but not hokey or too handmade looking. Watch the use of too many fonts and low-contrast colors with text on background.

```html
<!DOCTYPE html>
<html lang="en">
<head>
<meta charset="utf-8">
<title>Varubo Highlands – Dark Roast Bag</title>
<link rel="stylesheet" href="https://fonts.googleapis.com/css2?family=Cinzel:wght@400;700&display=swap">
<style>
  :root {
    --bg: #e9e9e6;
    --bag-black: #050505;
    --brand-red: #ec1f27;
    --brand-yellow: #ffcf3e;
    --brand-green: #9bcb3c;
    --white: #ffffff;
    --text-soft: #d9d9d9;
    --sky: #5f95d8;
    --cloud: #dfe8f2;
    --hill: #4f7a2c;
    --hill-dark: #23401a;
  }
  * { box-sizing: border-box; margin: 0; padding: 0; }
  html, body { width: 1200px; height: 1123px; overflow: hidden; }
  body {
    background: var(--bg);
    font-family: "Cinzel", serif;
    position: relative;
  }
  .bag-panel {
    position: absolute;
    top: 42px;
    width: 380px;
    height: 1040px;
    background: var(--bag-black);
    overflow: hidden;
    box-shadow: 0 6px 22px rgba(0,0,0,.25);
  }
  .bag-front { left: 190px; }
  .bag-back { left: 630px; }

  .landscape-photo {
    position: absolute;
    left: 0; top: 0; width: 100%;
  }
  .bag-front .landscape-photo {
    height: 620px;
    background: linear-gradient(180deg, var(--sky) 0%, var(--cloud) 18%, #cfdbe6 30%, var(--hill) 42%, var(--hill-dark) 70%, var(--bag-black) 100%);
  }
  .bag-back .landscape-photo {
    height: 330px;
    background: linear-gradient(180deg, var(--sky) 0%, var(--cloud) 22%, var(--hill) 45%, var(--hill-dark) 70%, var(--bag-black) 100%);
  }

  .brand-lockup {
    position: absolute;
    top: 330px; left: 0; width: 100%;
    text-align: center;
  }
  .brand-mark {
    width: 70px; height: 70px;
    margin: 0 auto 14px;
    border-radius: 50%;
    background: var(--brand-red);
  }
  .brand-name {
    font-weight: 700;
    font-size: 34px;
    color: var(--brand-red);
    letter-spacing: .5px;
  }
  .brand-tagline {
    margin-top: 4px;
    font-size: 13px;
    letter-spacing: 3px;
    color: var(--white);
  }

  .roast-title {
    position: absolute;
    top: 660px; width: 100%;
    text-align: center;
    font-size: 44px;
    color: var(--brand-red);
  }
  .roast-desc {
    position: absolute;
    top: 722px; width: 100%;
    text-align: center;
    font-size: 14px;
    letter-spacing: 1px;
    color: var(--brand-red);
  }
  .net-weight {
    position: absolute;
    top: 900px; right: 40px;
    font-size: 13px;
    color: var(--text-soft);
  }
  .grind-choice {
    position: absolute;
    top: 940px; left: 0; width: 100%;
    display: flex; justify-content: center; align-items: center; gap: 10px;
    font-size: 17px;
    color: var(--white);
  }
  .check-box {
    width: 13px; height: 13px;
    border: 1.5px solid var(--white);
    background: var(--white);
  }

  .origin-story {
    position: absolute;
    top: 330px; left: 30px; right: 30px;
    color: var(--text-soft);
    font-size: 13px;
    line-height: 1.45;
    text-align: justify;
  }
  .origin-story p + p { margin-top: 22px; }

  .origin-map {
    position: absolute;
    top: 610px; left: 40px;
    width: 300px; height: 330px;
    border-radius: 38% 30% 28% 40%;
    background: linear-gradient(160deg, var(--white) 0%, #f1f1f1 70%, var(--brand-green) 100%);
  }
  .partner-badge {
    position: absolute;
    top: 730px; left: 150px;
    width: 110px; height: 60px;
    background: var(--brand-yellow);
    border: 3px solid var(--brand-red);
  }
  .map-caption {
    position: absolute;
    top: 960px; left: 40px; right: 40px;
    padding: 8px 0;
    text-align: center;
    font-size: 12px;
    letter-spacing: 2px;
    color: var(--text-soft);
    border-top: 1px solid #333;
    border-bottom: 1px solid #333;
  }
</style>
</head>
<body>

<section class="bag-panel bag-front">
  <div class="landscape-photo" role="img" aria-label="Photo of green terraced highland hills under a blue sky with white clouds, fading into black"></div>
  <div class="brand-lockup">
    <div class="brand-mark"></div>
    <div class="brand-name">Varubo Highlands</div>
    <div class="brand-tagline">PREMIUM UGANDAN COFFEE</div>
  </div>
  <h1 class="roast-title">Dark Roast</h1>
  <p class="roast-desc">A bold, rich 100% Arabica blend</p>
  <p class="net-weight">Net Weight 250g | 9oz</p>
  <div class="grind-choice">
    <span class="check-box"></span>
    <span>Whole Bean | Ground</span>
    <span class="check-box"></span>
  </div>
</section>

<section class="bag-panel bag-back">
  <div class="landscape-photo" role="img" aria-label="Photo of terraced farmland valley with distant mountains, fading into black"></div>
  <div class="origin-story">
    <p>The Varubo Highlands of southwest Uganda produce exceptional coffee. Pure highland air blends with abundant sun, rain and fertile volcanic soils to produce remarkable beans with rich, bold, complex flavors.</p>
    <p>More than 2800 area farmers carefully select only the best beans, which are then dried and hand-roasted to become Varubo Highlands, a premium 100% Ugandan coffee.</p>
  </div>
  <div class="origin-map" role="img" aria-label="White map of Uganda with the Varubo region marked in green at the southwest"></div>
  <div class="partner-badge"></div>
  <p class="map-caption">Varubo Mountain Region</p>
</section>

</body>
</html>
```